Ridgeline Talent Associates Business Card Design

We need a business card design for our new company - Ridgeline Talent Associates. RLTA is a recruitment firm that focuses on recruiting engineers and geologist for mid-size oil and gas companies. We would like our logo on the business card, which is attached, and we would like the color scheme on business cards to coordinate with our logo.

Industry/Entity Type

Oil And Gas

Contact Information for Business Card

Dana Whitlow, Founder and Managing Partner, dmw@ridgelinetalentco.org, 888.507.3942 (work), 5730915.0600 (cell), 573.642.1907 (fax), www.ridgelinetalentco.org

```html
<!DOCTYPE html>
<html lang="en">
<head>
<meta charset="utf-8">
<title>Ridgeline Talent Associates – Business Card</title>
<link href="https://fonts.googleapis.com/css2?family=Exo+2:wght@400;500;600&display=swap" rel="stylesheet">
<style>
  :root {
    --navy: #2b2d5c;
    --ink: #2a2a2e;
    --card: #ffffff;
    --card-shade: #f1f2f4;
    --backdrop: #5c5d60;
    --logo-dot: #3a3d78;
  }
  * { box-sizing: border-box; margin: 0; padding: 0; }
  html, body { width: 1200px; height: 675px; overflow: hidden; }
  body {
    background: var(--backdrop);
    font-family: "Exo 2", sans-serif;
    color: var(--ink);
    position: relative;
  }
  .card {
    position: absolute;
    top: 187px;
    width: 520px;
    height: 300px;
    border-radius: 28px;
    background: linear-gradient(160deg, var(--card) 40%, var(--card-shade));
    overflow: hidden;
  }
  .card--front { left: 50px; }
  .card--back { left: 630px; background: var(--card); }

  .bubble-frame { position: absolute; left: 0; top: 0; }

  .brand {
    position: absolute;
    display: flex;
    align-items: center;
    gap: 10px;
    color: var(--navy);
    font-weight: 600;
    text-transform: uppercase;
    letter-spacing: 0.04em;
    white-space: nowrap;
  }
  .brand__dot {
    border-radius: 50%;
    background: var(--logo-dot);
    flex: none;
  }
  .card--front .brand { left: 40px; top: 40px; font-size: 15px; }
  .card--front .brand__dot { width: 34px; height: 34px; }
  .card--back .brand {
    left: 0; right: 0; top: 130px;
    justify-content: center;
    font-size: 18px;
  }
  .card--back .brand__dot { width: 40px; height: 40px; }

  .person {
    position: absolute;
    right: 40px;
    top: 92px;
    white-space: nowrap;
  }
  .person__name { font-size: 23px; font-weight: 500; letter-spacing: 0.05em; text-transform: uppercase; line-height: 1.1; }
  .person__title { font-size: 9.5px; font-weight: 500; letter-spacing: 0.06em; text-transform: uppercase; margin-top: 3px; }

  .contact-list { position: absolute; list-style: none; font-size: 13px; white-space: nowrap; }
  .contact-list li { display: flex; align-items: center; gap: 10px; margin-bottom: 6px; line-height: 16px; }
  .contact-list svg { width: 14px; height: 14px; flex: none; }
  .contact-list--phones { left: 36px; top: 172px; }
  .contact-list--online { left: 262px; top: 192px; }

  .divider {
    position: absolute;
    left: 238px; top: 186px;
    height: 44px;
    border-left: 3px dotted var(--ink);
  }
  .address {
    position: absolute;
    left: 36px; bottom: 18px;
    font-size: 13px;
    letter-spacing: 0.02em;
    white-space: nowrap;
  }
</style>
</head>
<body>

<section class="card card--front" aria-label="Business card front">
  <svg class="bubble-frame" width="520" height="300" viewBox="0 0 520 300" aria-hidden="true">
    <path d="M40 16 H480 A24 24 0 0 1 504 40 V136 A24 24 0 0 1 480 160 H270 L240 182 L212 160 H40 A24 24 0 0 1 16 136 V40 A24 24 0 0 1 40 16 Z"
          fill="none" stroke="var(--navy)" stroke-width="2"/>
  </svg>

  <div class="brand">
    <span class="brand__dot"></span>
    <span class="brand__name">Ridgeline Talent Associates</span>
  </div>

  <div class="person">
    <p class="person__name">Dana Whitlow</p>
    <p class="person__title">Founder and Managing Partner</p>
  </div>

  <ul class="contact-list contact-list--phones">
    <li>
      <svg viewBox="0 0 24 24"><path d="M6.6 10.8a15 15 0 0 0 6.6 6.6l2.2-2.2a1 1 0 0 1 1-.25 11 11 0 0 0 3.6.6 1 1 0 0 1 1 1V20a1 1 0 0 1-1 1A17 17 0 0 1 3 4a1 1 0 0 1 1-1h3.5a1 1 0 0 1 1 1 11 11 0 0 0 .6 3.6 1 1 0 0 1-.25 1z" fill="var(--ink)"/></svg>
      <span>888.507.3942</span>
    </li>
    <li>
      <svg viewBox="0 0 24 24"><rect x="6" y="2" width="12" height="20" rx="2" fill="none" stroke="var(--ink)" stroke-width="2"/><circle cx="12" cy="18" r="1.2" fill="var(--ink)"/></svg>
      <span>5730915.0600</span>
    </li>
    <li>
      <svg viewBox="0 0 24 24" fill="none" stroke="var(--ink)" stroke-width="2"><path d="M7 9V3h10v6"/><rect x="3" y="9" width="18" height="8" rx="1"/><path d="M7 14h10v7H7z" fill="#fff"/></svg>
      <span>573.642.1907</span>
    </li>
  </ul>

  <span class="divider" aria-hidden="true"></span>

  <ul class="contact-list contact-list--online">
    <li>
      <svg viewBox="0 0 24 24"><rect x="2" y="5" width="20" height="14" rx="1" fill="var(--ink)"/><path d="M2 6 L12 13 L22 6" fill="none" stroke="#fff" stroke-width="1.6"/></svg>
      <span>dmw@ridgelinetalentco.org</span>
    </li>
    <li>
      <svg viewBox="0 0 24 24" fill="none" stroke="var(--ink)" stroke-width="1.8"><circle cx="12" cy="12" r="9.5"/><ellipse cx="12" cy="12" rx="4" ry="9.5"/><path d="M2.5 12h19M4 7h16M4 17h16"/></svg>
      <span>www.ridgelinetalentco.org</span>
    </li>
  </ul>

  <p class="address">214 Cedar Hollow Road, Suite 3B</p>
</section>

<section class="card card--back" aria-label="Business card back">
  <div class="brand">
    <span class="brand__dot"></span>
    <span class="brand__name">Ridgeline Talent Associates</span>
  </div>
</section>

</body>
</html>
```